Corporate Profile

We are an Electrical Engineering company and we require a rework on our company profile urgently. We need it be have a nice modern look and feel.

We do not have much time as we need the brochures ready printed before 24th Oct 2014.

Please find attached a .pdf file with our company profile and a complimetary slip that has our high definition logo to be extracted.

1. We require a front page design. 2. There is no particular size. You can suggest on the size.

Electrical

```html
<!DOCTYPE html>
<html lang="en">
<head>
<meta charset="utf-8">
<title>Voltara Energy Brochure Design_01</title>
<link href="https://fonts.googleapis.com/css2?family=Arimo:wght@400;700&family=Tinos&display=swap" rel="stylesheet">
<style>
  :root {
    --red: #d0232a;
    --ink: #111111;
    --body-grey: #b4b4b4;
    --rule: #c9c9c9;
    --board: #ffffff;
    --page: #ffffff;
    --blue: #5fb6e6;
    --violet: #7d4fc4;
    --magenta: #d2338f;
    --orange: #f08a2c;
  }
  * { box-sizing: border-box; margin: 0; padding: 0; }
  html, body { width: 1200px; height: 1000px; overflow: hidden; background: var(--board); }
  body { position: relative; font-family: "Arimo", Arial, sans-serif; }

  .board-title, .page-caption {
    position: absolute; font-family: "Tinos", "Times New Roman", serif;
    font-size: 20px; color: var(--ink); text-align: center;
  }
  .board-title { left: 0; width: 1200px; top: 226px; }
  .page-caption { top: 754px; width: 564px; }
  .caption-cover { left: 24px; }
  .caption-inside { left: 612px; }

  .spread {
    position: absolute; top: 268px; width: 564px; height: 466px;
    background: var(--page); overflow: hidden;
    box-shadow: 2px 3px 5px rgba(0,0,0,.35);
  }
  .spread-cover { left: 24px; }
  .spread-inside { left: 612px; }

  .wordmark {
    position: absolute; top: 28px; font-weight: 700; font-size: 11px;
    line-height: 11px; color: var(--red); letter-spacing: .5px; width: 80px;
  }

  .contact { position: absolute; left: 24px; top: 108px; font-size: 6px; line-height: 8.6px; color: var(--ink); }
  .contact .lead { margin-bottom: 6px; }
  .contact strong { font-weight: 700; }

  .headline { position: absolute; left: 329px; top: 106px; font-weight: 700; font-size: 20px; line-height: 22px; }
  .headline .brand-line { color: var(--red); }
  .headline .tagline { color: var(--ink); margin-top: 3px; }

  .energy-wave {
    position: absolute; left: 0; width: 564px;
    background: linear-gradient(90deg, var(--blue) 0%, #8fd0f0 12%, var(--violet) 32%, var(--magenta) 58%, #e8403a 76%, var(--orange) 100%);
    -webkit-mask-image: linear-gradient(180deg, transparent 0%, #000 40%, #000 62%, transparent 100%);
    mask-image: linear-gradient(180deg, transparent 0%, #000 40%, #000 62%, transparent 100%);
  }
  .spread-cover .energy-wave { top: 190px; height: 230px; }
  .spread-inside .energy-wave { top: 190px; height: 190px; opacity: .28; }

  .benefits { position: absolute; left: 329px; top: 402px; font-weight: 700; font-size: 8px; line-height: 11px; color: var(--ink); }
  .web { position: absolute; left: 24px; top: 435px; font-size: 8px; color: var(--red); }

  .column { position: absolute; top: 0; width: 234px; }
  .column-left { left: 24px; }
  .column-right { left: 306px; }
  .column-bar { height: 7px; background: var(--red); }
  .section-title { font-weight: 700; font-size: 20px; color: var(--red); margin-top: 21px; line-height: 22px; }
  .section-title + p { margin-top: 6px; }
  .column p { font-weight: 700; font-size: 8.4px; line-height: 9.9px; color: var(--body-grey); margin-bottom: 9.9px; }
  .column .section-title.mission { margin-top: 10px; }

  .page-foot { position: absolute; top: 442px; width: 234px; border-top: 1px solid var(--rule); font-size: 5px; color: var(--red); padding-top: 2px; }
  .foot-left { left: 24px; }
  .foot-right { left: 306px; text-align: right; }
</style>
</head>
<body>
  <h1 class="board-title">Voltara Energy Brochure Design_01</h1>

  <section class="spread spread-cover">
    <div class="energy-wave" role="img" aria-label="Flowing light-wave graphic in blue, violet, magenta and orange"></div>
    <div class="wordmark" style="left:24px;">VOLTARA ENERGY</div>
    <div class="wordmark" style="left:464px;">VOLTARA ENERGY</div>

    <div class="contact">
      <p class="lead">To find out more contact:</p>
      <p><strong>Voltara Electrical &amp; Supplies Limited</strong></p>
      <p>P.O. Box 12034 – 00200, Lakeside, Kenya</p>
      <p>Tel (Industrial Area): +254 (20) 5550142/7, 5550198</p>
      <p>Tel (Town Office): +254 (20) 5550231/5550264</p>
      <p>Fax (Industrial Area): +254 (20) 5550310</p>
      <p>Fax (Town Office): +254 (20) 5550264</p>
      <p>Email: hello@voltaraenergy.example</p>
    </div>

    <div class="headline">
      <div class="brand-line">Voltara Energy<br>Solutions.</div>
      <div class="tagline">The power<br>to save.</div>
    </div>

    <div class="benefits">Reduce cost<br>Improve efficiency<br>Embrace sustainability</div>
    <div class="web">www.voltaraenergy.example</div>
  </section>

  <section class="spread spread-inside">
    <div class="energy-wave" role="img" aria-label="Faint flowing light-wave graphic in pale blue and pink"></div>

    <article class="column column-left">
      <div class="column-bar"></div>
      <h2 class="section-title">History</h2>
      <p>Voltara Energy started as an electrical product sales company in 1991. Voltara Energy has evolved to be a complete electrical engineering company with its offices in Industrial area, Lakeside, Kenya.</p>
      <p>Voltara Energy deals in a broad range of electrical products for domestic, commercial and industrial applications.</p>
      <p>Voltara Energy has also over the years become a major solution provider for industries, commercial and domestic setups by helping them identify various ways of cutting costs through the saving of energy. Through conducting comprehensive Power Quality Analysis (PQA) and Energy Audits we are able to advice our customers on the various ways to reduce their power quality problems and the various energy saving opportunities available to them therefore helping them improve their overall efficiency.</p>
      <p>Since inception Voltara Energy has built a strong engineering team that has well established knowledge in the electrical engineering field and is able to apply its knowledge to the actual situation.</p>
      <p>Voltara Energy has a well established market throughout Kenya for 20 years since its inception.</p>
    </article>

    <article class="column column-right">
      <div class="column-bar"></div>
      <h2 class="section-title">Vision</h2>
      <p>To be a leading company in providing electrical energy efficiency solutions by the year 2030.</p>
      <h2 class="section-title mission">Mission</h2>
      <p>To spread out our market throughout Africa, both in market share and reputation, while providing maximum return on investment.</p>
      <p>Our Focus is providing general electrical solutions for domestic, commercial and industrial consumers and also utility providers.</p>
      <p>Voltara Energy will achieve its goals by carefully understanding and meeting the needs of our overall market and offering the benefits of proven advance technologies that suits the market. We will transform our customers' efficiency and productivity to sustainable world-class standards.</p>
    </article>

    <div class="page-foot foot-left">1</div>
    <div class="page-foot foot-right">2</div>
  </section>

  <p class="page-caption caption-cover">Front and Back Cover Page</p>
  <p class="page-caption caption-inside">Inside Pages</p>
</body>
</html>
```